Need Web Design for Business Process Outsourcing Company (Korvenza)

Korvenza is a business process outsourcing company. Need a simple site similar to http://www.taskmeridianhub.com/ but with a more professional and credible look. New to the process; not sure where to start and comparing my options. Please let me know what my options are if I choose to go with you. Logo is attached for your reference. Please use same colorway

Reason: I want the final product to be coded. Please confirm you will be able to code final design.

Industry/Entity Type

Business

Coding

Coded - Design and coding required

```html
<!DOCTYPE html>
<html lang="en">
<head>
<meta charset="utf-8">
<title>Korvenza Services</title>
<link href="https://fonts.googleapis.com/css2?family=Open+Sans:ital,wght@0,400;0,600;0,700;1,400;1,700&display=swap" rel="stylesheet">
<style>
:root{
  --blue:#1b8fd6;
  --blue-deep:#125f9e;
  --ink:#333;
  --muted:#8a8a8a;
  --light:#f4f5f6;
  --line:#e2e2e2;
  --topbar:#3b3b3b;
  --footer:#2c2c2c;
  --footer-base:#222;
  --white:#fff;
}
*{margin:0;padding:0;box-sizing:border-box}
html,body{width:1200px;height:2848px;overflow:hidden}
body{font-family:"Open Sans",Arial,sans-serif;color:var(--ink);background:var(--white)}
section,header,footer,.topbar{position:relative;width:1200px}

.topbar{height:32px;background:var(--topbar);color:#bbb;font-size:11px;display:flex;align-items:center;padding:0 40px;gap:28px}
.topbar .email{margin-left:auto}
.topbar span{display:flex;align-items:center;gap:6px}

.site-header{height:88px;display:flex;align-items:center;padding:0 40px;border-bottom:1px solid var(--line)}
.brand{display:flex;align-items:center;gap:10px;font-size:26px;font-weight:700;color:var(--blue)}
.brand i{width:26px;height:26px;background:var(--blue);border-radius:4px;display:block}
.main-nav{margin-left:auto;display:flex;font-size:11px;text-transform:uppercase;letter-spacing:.5px;color:#777}
.main-nav a{padding:0 14px;border-left:1px solid #ddd;color:inherit;text-decoration:none}
.main-nav a:first-child{border-left:0}
.main-nav a.active{color:var(--blue);font-weight:600}

.hero{height:500px;background:linear-gradient(160deg,#6fb8e8 0%,#2f8ad1 45%,#1b5f9c 100%);color:var(--white);text-align:center}
.hero-img{position:absolute;inset:0}
.hero-copy{position:absolute;top:140px;left:0;right:0}
.hero h1{font-size:30px;font-weight:700;letter-spacing:1px}
.hero p{font-size:14px;margin-top:10px;font-weight:600}
.btn{display:inline-block;background:var(--blue);color:var(--white);font-size:11px;font-weight:600;padding:9px 22px;text-transform:uppercase;border:1px solid rgba(255,255,255,.6)}
.hero .btn{margin-top:34px}
.dots{display:flex;gap:7px;justify-content:center}
.dots i{width:9px;height:9px;border-radius:50%;background:rgba(255,255,255,.55);display:block}
.dots i.on{background:var(--white)}
.hero .dots{position:absolute;bottom:52px;left:0;right:0}

.who{height:220px;background:var(--light);padding:60px 100px 0}
.section-title{font-size:28px;font-weight:600;color:var(--ink)}
.who p{font-size:13px;color:#666;line-height:1.6;width:800px;margin-top:16px}
.who .dots{position:absolute;right:100px;top:162px}
.who .dots i{background:#bcd9ee}
.who .dots i.on{background:var(--blue)}

.solutions{height:480px;text-align:center;padding-top:100px}
.solution-row{display:flex;justify-content:center;margin-top:70px;position:relative}
.solution{width:240px;display:flex;flex-direction:column;align-items:center;position:relative}
.solution + .solution::before{content:"";position:absolute;left:-60px;top:38px;width:120px;border-top:1px solid #ccc}
.solution span{font-size:18px;color:#555;margin-top:22px}
.arrow{position:absolute;top:50%;color:#999}
.solutions .arrow{top:250px}
.arrow.left{left:58px}.arrow.right{right:58px}

.stats{height:180px;background:linear-gradient(100deg,#0f5a97 0%,#1a78c2 50%,#12609f 100%);display:flex;justify-content:center;align-items:center;color:var(--white)}
.stat{width:240px;text-align:center;border-left:1px solid rgba(255,255,255,.3)}
.stat:first-child{border-left:0}
.stat b{display:block;font-size:48px;font-weight:600;line-height:1}
.stat small{font-size:11px;display:block;margin-top:12px}

.news{height:580px;text-align:center;padding-top:64px;background:var(--white)}
.news-cards{display:flex;justify-content:center;gap:55px;margin-top:44px;text-align:left}
.card{width:250px}
.card-img{height:168px;background:linear-gradient(135deg,#c9d3dd,#8a9bb0)}
.card:nth-child(3) .card-img{background:linear-gradient(160deg,#7fb2de,#a48a5e)}
.card h3{font-size:16px;font-weight:700;margin-top:16px}
.card p{font-size:12px;color:#777;line-height:1.55;margin-top:8px}
.meta{display:flex;gap:22px;font-size:11px;color:#999;margin-top:14px}
.meta span{display:flex;align-items:center;gap:5px}
.news .arrow{top:360px}

.testimonials{height:420px;padding:90px 100px 0;border-top:1px solid var(--line)}
.testimonials .nav-arrows{position:absolute;right:100px;top:100px;color:#999;display:flex;gap:10px}
.quote{position:relative;margin-top:44px;width:900px;height:110px;background:#ececec;padding:24px 140px 0 60px;font-size:12px;font-style:italic;color:#666;line-height:1.6}
.quote::before{content:"\201C";position:absolute;left:24px;top:10px;font-size:44px;color:#999;font-style:normal}
.avatar{position:absolute;left:910px;top:170px;width:90px;height:90px;border-radius:50%;background:linear-gradient(160deg,#c4ccd6,#53667c);border:4px solid var(--blue)}
.author{position:absolute;left:760px;top:300px;font-size:13px;color:var(--blue);font-style:italic}

.site-footer{height:300px;background:var(--footer);color:#ccc;display:flex;padding:60px 100px 0;gap:0}
.footer-col{width:440px}
.footer-col:nth-child(2){width:340px}
.footer-col h4{font-size:18px;font-weight:400;color:var(--white);margin-bottom:24px}
.field{width:260px;height:36px;background:var(--white);font-size:11px;color:#aaa;padding:10px 12px}
.footer-col .btn{margin-top:14px;border:0}
.contact b{display:block;font-style:italic;color:var(--white);font-size:14px;margin-bottom:6px}
.contact p{font-size:13px;line-height:1.6}
.social{display:flex;gap:22px}
.social i{width:30px;height:30px;border-radius:50%;background:var(--white);display:block}

.copyright{height:48px;background:var(--footer-base);color:#bbb;font-size:12px;display:flex;align-items:center;padding:0 100px}
</style>
</head>
<body>

<div class="topbar">
  <span><svg width="10" height="10" viewBox="0 0 10 10"><path d="M2 0l2 2-1 1.5a6 6 0 003.5 3.5L8 6l2 2-1.5 2C4 10 0 6 0 1.5z" fill="#bbb"/></svg>(555) 123-4567</span>
  <span><svg width="8" height="11" viewBox="0 0 8 11"><path d="M4 0a4 4 0 014 4c0 3-4 7-4 7S0 7 0 4a4 4 0 014-4z" fill="#bbb"/><circle cx="4" cy="4" r="1.5" fill="#3b3b3b"/></svg>48 Larkfield Avenue, Ashbury, OR 97512</span>
  <span class="email">info@korvenza.com</span>
</div>

<header class="site-header">
  <div class="brand"><i></i>Korvenza</div>
  <nav class="main-nav">
    <a class="active" href="#">Who We Are</a>
    <a href="#">Solutions</a>
    <a href="#">Strategy</a>
    <a href="#">Our Experience</a>
    <a href="#">News</a>
    <a href="#">Contact Us</a>
  </nav>
</header>

<section class="hero">
  <div class="hero-img" role="img" aria-label="Glass office tower against a blue sky"></div>
  <div class="hero-copy">
    <h1>LOREM LIPSUM</h1>
    <p>Lorem Ipsum is simply dummy text of the printing and typesetting industry</p>
    <a class="btn" href="#">Read More</a>
  </div>
  <div class="dots"><i class="on"></i><i></i><i></i></div>
</section>

<section class="who">
  <h2 class="section-title">Who We Are</h2>
  <p>Lorem Ipsum is simply dummy text of the printing and typesetting industry. Lorem Ipsum has been the industry's standard dummy text ever since the 1500s, when an unknown printer took a galley of type and scrambled it to make a type specimen book</p>
  <div class="dots"><i class="on"></i><i></i></div>
</section>

<section class="solutions">
  <h2 class="section-title">Our Solutions</h2>
  <div class="solution-row">
    <div class="solution">
      <svg width="76" height="76" viewBox="0 0 76 76" fill="none" stroke="#1b8fd6" stroke-width="5"><path d="M14 44V36a24 24 0 0148 0v8"/><rect x="8" y="40" width="12" height="20" rx="4" fill="#1b8fd6"/><rect x="56" y="40" width="12" height="20" rx="4" fill="#1b8fd6"/><path d="M62 60c0 8-10 10-20 10"/></svg>
      <span>Customer<br>Service</span>
    </div>
    <div class="solution">
      <svg width="76" height="76" viewBox="0 0 76 76" fill="none" stroke="#1b8fd6" stroke-width="5"><path d="M6 14h10l8 36h38l6-26H22"/><circle cx="30" cy="62" r="5" fill="#1b8fd6"/><circle cx="56" cy="62" r="5" fill="#1b8fd6"/><path d="M44 24v18M35 33h18"/></svg>
      <span>Ecommerce</span>
    </div>
    <div class="solution">
      <svg width="76" height="76" viewBox="0 0 76 76" fill="none" stroke="#1b8fd6" stroke-width="4"><rect x="6" y="12" width="64" height="44" rx="3"/><path d="M28 66h20M38 56v10M30 26l-8 8 8 8M46 26l8 8-8 8"/></svg>
      <span>IT Solutions</span>
    </div>
    <div class="solution">
      <svg width="76" height="76" viewBox="0 0 76 76" fill="#1b8fd6"><circle cx="38" cy="14" r="8"/><rect x="28" y="24" width="20" height="16" rx="4"/><circle cx="16" cy="46" r="7"/><rect x="7" y="55" width="18" height="14" rx="4"/><circle cx="60" cy="46" r="7"/><rect x="51" y="55" width="18" height="14" rx="4"/><path d="M38 40v6M16 46V44h44v2" stroke="#1b8fd6" stroke-width="3" fill="none"/></svg>
      <span>Consulting</span>
    </div>
  </div>
  <svg class="arrow left" width="14" height="24" viewBox="0 0 14 24"><path d="M12 2L2 12l10 10" fill="none" stroke="#999" stroke-width="3"/></svg>
  <svg class="arrow right" width="14" height="24" viewBox="0 0 14 24"><path d="M2 2l10 10L2 22" fill="none" stroke="#999" stroke-width="3"/></svg>
</section>

<section class="stats">
  <div class="stat"><b>10</b><small>YEARS OF EXPERIENCE</small></div>
  <div class="stat"><b>55</b><small>Qualified Specialists</small></div>
  <div class="stat"><b>12</b><small>Lorem Ipsum Dummy Text</small></div>
  <div class="stat"><b>2</b><small>Century Build Issue</small></div>
</section>

<section class="news">
  <h2 class="section-title">Latest News</h2>
  <div class="news-cards">
    <article class="card">
      <div class="card-img" role="img" aria-label="Business team gathered around a laptop"></div>
      <h3>Lorem Ipsum is dummy text</h3>
      <p>It is a long established fact that a reader will be distracted by the readable content of a page when looking at its layout.</p>
      <div class="meta"><span>&#9719; Feb 16, 2016</span><span>&#9633; 03 Comments</span></div>
    </article>
    <article class="card">
      <div class="card-img" role="img" aria-label="Colleagues in a meeting room"></div>
      <h3>Lorem Ipsum is dummy text</h3>
      <p>It is a long established fact that a reader will be distracted by the readable content of a page when looking at its layout.</p>
      <div class="meta"><span>&#9719; Feb 16, 2016</span><span>&#9633; 03 Comments</span></div>
    </article>
    <article class="card">
      <div class="card-img" role="img" aria-label="Engineers on a construction site"></div>
      <h3>Lorem Ipsum is dummy text</h3>
      <p>It is a long established fact that a reader will be distracted by the readable content of a page when looking at its layout.</p>
      <div class="meta"><span>&#9719; Feb 16, 2016</span><span>&#9633; 03 Comments</span></div>
    </article>
  </div>
  <svg class="arrow left" width="14" height="24" viewBox="0 0 14 24"><path d="M12 2L2 12l10 10" fill="none" stroke="#999" stroke-width="3"/></svg>
  <svg class="arrow right" width="14" height="24" viewBox="0 0 14 24"><path d="M2 2l10 10L2 22" fill="none" stroke="#999" stroke-width="3"/></svg>
</section>

<section class="testimonials">
  <h2 class="section-title">Testimonials</h2>
  <div class="nav-arrows">
    <svg width="10" height="16" viewBox="0 0 10 16"><path d="M8 2L2 8l6 6" fill="none" stroke="#999" stroke-width="2"/></svg>
    <svg width="10" height="16" viewBox="0 0 10 16"><path d="M2 2l6 6-6 6" fill="none" stroke="#999" stroke-width="2"/></svg>
  </div>
  <div class="quote">Lorem Ipsum is simply dummy text of the printing and typesetting industry. Lorem Ipsum has been the industry's standard dummy text ever since the 1500s, when an unknown printer took a galley of type and scrambled it to make a type specimen book. It has survived not only five centuries, but also the leap into electronic, remaining essentially unchanged.</div>
  <div class="avatar" role="img" aria-label="Portrait of the client giving the testimonial"></div>
  <div class="author">Daniel Reyes - CEO Halden Company</div>
</section>

<footer class="site-footer">
  <div class="footer-col">
    <h4>Newsletter</h4>
    <div class="field">Email Address</div>
    <a class="btn" href="#">Subscribe</a>
  </div>
  <div class="footer-col contact">
    <h4>Contact Us</h4>
    <b>Korvenza Services</b>
    <p>T: 123-456-7890<br>E: info@korvenza.com</p>
  </div>
  <div class="footer-col">
    <h4>Social Media</h4>
    <div class="social"><i></i><i></i><i></i><i></i></div>
  </div>
</footer>

<div class="copyright">Copyrights 2016 Korvenza Services. All Rights Reserved</div>

</body>
</html>
```